ultra-minimalist business card

front (black background, matte):

tarik b. hosseny
writer | photographer
get@tarikhosseny.com

back (white background, matte):

a picture speaks a thousand words;
a word draws a thousand pictures.

www.tarikhosseny.com

all text should be small (white or silver - as long as it shows against the black - on the front; black or gray - as long as it shows against the white - on the back).

feel free to get creative in terms of arrangement, alignment, and font type, but remember, the overall style is minimalist, so nothing too fancy, please.

thanks.

```html
<!DOCTYPE html>
<html lang="en">
<head>
<meta charset="utf-8">
<title>tarik b. hosseny — business card</title>
<link rel="stylesheet" href="https://fonts.googleapis.com/css2?family=Open+Sans:wght@400;700&family=Roboto+Condensed:wght@400;500&display=swap">
<style>
  :root {
    --page: #ece9e4;
    --card-dark: #2b2d30;
    --card-light: #ffffff;
    --ink-white: #ffffff;
    --ink-silver: #b9bbbe;
    --ink-bar: #c9cacc;
    --ink-dark: #4a4a4a;
    --ink-grey: #a3a3a3;
    --ink-url: #2b2b2b;
    --shadow: 0 18px 40px rgba(0,0,0,.22), 0 3px 8px rgba(0,0,0,.15);
  }
  * { box-sizing: border-box; margin: 0; padding: 0; }
  html, body { width: 1200px; height: 844px; overflow: hidden; }
  body {
    background: var(--page);
    display: flex;
    align-items: center;
    justify-content: center;
    gap: 44px;
  }
  .card {
    position: relative;
    width: 540px;
    height: 309px;
    box-shadow: var(--shadow);
  }

  /* front */
  .card--front { background: var(--card-dark); font-family: "Open Sans", sans-serif; }
  .front__bar {
    position: absolute; left: 22px; top: 104px;
    width: 9px; height: 78px; background: var(--ink-bar);
  }
  .front__identity { position: absolute; left: 92px; top: 100px; }
  .front__name {
    font-size: 31px; font-weight: 700; letter-spacing: -1.6px;
    line-height: 1; color: var(--ink-white);
  }
  .front__name-first { color: var(--ink-silver); }
  .front__roles {
    margin-top: 4px; margin-left: 6px;
    font-size: 15px; color: var(--ink-white); letter-spacing: .2px;
  }
  .front__divider { color: var(--ink-silver); margin: 0 12px; }
  .front__contact {
    position: absolute; left: 190px; bottom: 34px;
    display: flex; align-items: center; gap: 10px;
    font-size: 13px; color: var(--ink-white);
  }
  .front__contact-rule { width: 1px; height: 20px; background: var(--ink-silver); }
  .icon-mail { width: 22px; height: 16px; }

  /* back */
  .card--back { background: var(--card-light); }
  .back__quote {
    position: absolute; right: 46px; top: 100px;
    font-family: "Roboto Condensed", sans-serif;
    font-size: 31px; font-weight: 500; letter-spacing: -1.8px;
    line-height: .92; color: var(--ink-grey); text-align: right;
  }
  .back__quote-line { display: block; }
  .back__quote-line--second { margin-right: -8px; }
  .back__key { color: var(--ink-dark); }
  .back__web {
    position: absolute; left: 0; right: 0; bottom: 62px;
    display: flex; align-items: center; justify-content: center; gap: 12px;
    padding-left: 120px;
    font-family: "Open Sans", sans-serif; font-size: 13px; color: var(--ink-url);
  }
  .back__web-rule { width: 18px; height: 1px; background: var(--ink-url); }
</style>
</head>
<body>
  <section class="card card--front" aria-label="Card front">
    <div class="front__bar"></div>
    <div class="front__identity">
      <h1 class="front__name"><span class="front__name-first">tarik</span> b. hosseny</h1>
      <p class="front__roles">writer<span class="front__divider">|</span>photographer</p>
    </div>
    <div class="front__contact">
      <svg class="icon-mail" viewBox="0 0 22 16" aria-hidden="true">
        <rect x="0.75" y="0.75" width="20.5" height="14.5" fill="none" stroke="#b9bbbe" stroke-width="1.2"/>
        <path d="M1 1 L11 9 L21 1 M1 15 L8.5 7 M21 15 L13.5 7" fill="none" stroke="#b9bbbe" stroke-width="1.2"/>
      </svg>
      <span class="front__contact-rule"></span>
      <span class="front__email">get@tarikhosseny.com</span>
    </div>
  </section>

  <section class="card card--back" aria-label="Card back">
    <p class="back__quote">
      <span class="back__quote-line">a <span class="back__key">picture</span> speaks a thousand <span class="back__key">words</span></span>
      <span class="back__quote-line back__quote-line--second">a <span class="back__key">word</span> draws a thousand <span class="back__key">pictures</span></span>
    </p>
    <div class="back__web">
      <span class="back__web-rule"></span>
      <span>www.tarikhosseny.com</span>
      <span class="back__web-rule"></span>
    </div>
  </section>
</body>
</html>
```